Business Card Design

Contact Information for Business Card

A vertical business card request- a medium & light gray with silverfern tree logo (logo is attached)

Please use Trebuchet font -- if possible- can we use two different color gray? (See pictures attached below)
Info on the front should be the Silverfern tree logo - on the top of the card, followed by the info ...
Card to read: " " indicated what should be on the card --
Name: " Joan Pelley "
Title : "Partner "
" Office: 202.555.0147 "
" Mobile: 202.555.0182 "

Backside of the card - solid medium color gray color w/ address and small message centered in the card - Trebuchet font
to read:

" 317 B North Linden Avenue, NE "
" Washington, DC 20099 "

Then below address to read:
" Fundraising | Event Planning | Political Consulting "

```html
<!DOCTYPE html>
<html lang="en">
<head>
<meta charset="utf-8">
<title>Northgate Advisors – Business Card</title>
<link rel="stylesheet" href="https://fonts.googleapis.com/css2?family=Fira+Sans:wght@400;600&display=swap">
<style>
  :root {
    --backdrop: #d38c5d;
    --gray-medium: #7b7b7b;
    --gray-light: #f4f4f2;
    --ink: #3a3a3a;
    --ink-soft: #4a4a4a;
    --on-gray: #ffffff;
    --on-gray-soft: #dcdcdc;
  }
  * { box-sizing: border-box; margin: 0; padding: 0; }
  html, body {
    width: 1200px; height: 1200px; overflow: hidden;
    background: var(--backdrop);
    font-family: "Fira Sans", "Trebuchet MS", sans-serif;
  }
  .sheet {
    width: 1200px; height: 1200px;
    display: flex; align-items: center; justify-content: center; gap: 80px;
  }
  .card {
    width: 380px; height: 664px;
    position: relative; overflow: hidden;
    box-shadow: 0 10px 30px rgba(0,0,0,0.18);
  }

  /* Front */
  .card-front { background: var(--gray-light); }
  .brand-panel {
    position: absolute; inset: 0 0 auto 0; height: 376px;
    background: var(--gray-medium);
  }
  .brand-name {
    position: absolute; left: 36px; bottom: 30px;
    display: flex; align-items: center; gap: 12px;
    color: var(--on-gray);
    font-weight: 400; font-size: 26px; line-height: 1;
  }
  .brand-name .square {
    width: 14px; height: 14px; background: var(--on-gray);
  }
  .contact {
    position: absolute; left: 36px; top: 418px; color: var(--ink);
  }
  .contact-name { font-weight: 600; font-size: 25px; }
  .contact-title { font-size: 19px; color: var(--ink-soft); margin-top: 4px; }
  .contact-lines { margin-top: 38px; font-size: 20px; line-height: 1.3; color: var(--ink-soft); }

  /* Back */
  .card-back { background: var(--gray-medium); }
  .back-info {
    position: absolute; left: 0; right: 0; bottom: 120px;
    text-align: center; color: var(--on-gray);
  }
  .address { font-size: 19px; line-height: 1.35; }
  .services {
    margin-top: 18px; font-size: 11px; letter-spacing: 1px;
    text-transform: uppercase; color: var(--on-gray-soft);
  }
</style>
</head>
<body>
<main class="sheet">
  <section class="card card-front" aria-label="Card front">
    <div class="brand-panel">
      <div class="brand-name"><span class="square"></span><span>Northgate Advisors</span></div>
    </div>
    <div class="contact">
      <p class="contact-name">Joan Pelley</p>
      <p class="contact-title">Partner</p>
      <div class="contact-lines">
        <p>202.555.0147 office</p>
        <p>202.555.0182 mobile</p>
        <p>joan@silverfernllc.com</p>
      </div>
    </div>
  </section>

  <section class="card card-back" aria-label="Card back">
    <div class="back-info">
      <p class="address">317 B North Linden Avenue, NE<br>Washington, DC 20099</p>
      <p class="services">Fundraising | Event Planning | Political Consulting</p>
    </div>
  </section>
</main>
</body>
</html>
```